Vela Stewardship Business Card design

We need a creative business card design for our hospitality management company
We need the following information:
Our business Logo: Vela Stewardship
Name: Mara Dobrinsky
Phone number: 0458 317 642
Email: mara@velastewardship.com.au
Address: 214/53 Penrose Street, South Melbourne 3206
Web: www.velastewardship.com.au
I need the design to be a working file so that I can insert the names and numbers of the other staff members of our business.
The cards need to be 90 x 40mm
Thanks
Industry/Entity Type
Hospitality
Look and feel

```html
<!DOCTYPE html>
<html lang="en">
<head>
<meta charset="utf-8">
<title>Vela Stewardship – Business Card</title>
<link rel="stylesheet" href="https://fonts.googleapis.com/css2?family=Roboto+Condensed:wght@700&display=swap">
<style>
  :root {
    --orange: #ff9408;
    --white: #ffffff;
    --ink-blue: #1f5fa8;
    --navy: #0e2e5c;
    --backdrop: #f1f1f1;
  }
  html, body {
    margin: 0;
    padding: 0;
    width: 1200px;
    height: 900px;
    overflow: hidden;
    background: var(--backdrop);
  }
  .canvas {
    position: relative;
    width: 1200px;
    height: 900px;
    font-family: "Roboto Condensed", "Arial Narrow", sans-serif;
    font-weight: 700;
  }
  .card {
    position: absolute;
    width: 945px;
    height: 420px;
    border-radius: 18px;
    overflow: hidden;
    box-shadow: 0 4px 12px rgba(0, 0, 0, 0.18);
  }
  .card--front { left: 30px; top: 20px; }
  .card--back { left: 225px; top: 460px; }
  .card__ground {
    position: absolute;
    inset: 0;
    width: 100%;
    height: 100%;
  }
  .brand {
    position: absolute;
    left: 0;
    right: 0;
    top: 22px;
    display: flex;
    flex-direction: column;
    align-items: center;
  }
  .brand__mark {
    width: 150px;
    height: 150px;
    background: var(--navy);
  }
  .brand__name {
    margin: 38px 0 0;
    font-size: 96px;
    line-height: 1;
    letter-spacing: 1px;
    color: var(--navy);
    text-transform: uppercase;
    white-space: nowrap;
  }
  .contact {
    position: absolute;
    margin: 0;
    color: var(--ink-blue);
    white-space: nowrap;
    line-height: 1;
  }
  .contact__name { left: 158px; top: 52px; font-size: 58px; }
  .contact__phone { left: 145px; top: 122px; font-size: 40px; }
  .contact__email { left: 132px; top: 168px; font-size: 40px; }
  .contact__address {
    right: 128px;
    top: 242px;
    font-size: 32px;
    line-height: 1.15;
    text-align: right;
    font-style: normal;
  }
  .contact__web { right: 150px; top: 335px; font-size: 42px; }
</style>
</head>
<body>
<main class="canvas">

  <section class="card card--front" aria-label="Card front">
    <svg class="card__ground" viewBox="0 0 945 420" preserveAspectRatio="none" aria-hidden="true">
      <rect width="945" height="420" fill="var(--orange)"/>
      <ellipse cx="472" cy="210" rx="372" ry="335" fill="var(--white)"/>
      <ellipse cx="472" cy="210" rx="345" ry="318" fill="none" stroke="var(--orange)" stroke-width="6"/>
    </svg>
    <div class="brand">
      <div class="brand__mark"></div>
      <h1 class="brand__name">Vela Stewardship</h1>
    </div>
  </section>

  <section class="card card--back" aria-label="Card back">
    <svg class="card__ground" viewBox="0 0 945 420" preserveAspectRatio="none" aria-hidden="true">
      <rect width="945" height="420" fill="var(--orange)"/>
      <ellipse cx="472" cy="210" rx="372" ry="335" fill="var(--white)"/>
      <ellipse cx="472" cy="210" rx="345" ry="318" fill="none" stroke="var(--orange)" stroke-width="6"/>
    </svg>
    <h2 class="contact contact__name">Mara Dobrinsky</h2>
    <p class="contact contact__phone">P: 0458 317 642</p>
    <p class="contact contact__email">E: mara@velastewardship.com.au</p>
    <address class="contact contact__address">214/53 Penrose Street<br>South Melbourne 3206</address>
    <p class="contact contact__web">www.velastewardship.com.au</p>
  </section>

</main>
</body>
</html>
```